Beauty Salon Design

The business card design will be for a new beauty salon opening up.

The therapist has over 11 years at a leading beauty Salon in perth.

The two colours that the salon will use is black and gold.

Industry/Entity Type

Beauty Salon

Contact Information for Business Card

Velmora Beauty

Corinne Ashdale
Advanced beauty therapist
0457 318 042

Monday - Friday 9am - 2.30pm
Weekends and nights by appointment only

Waxing, Tinting, Swedish massage, hot stone massage, facials, peels, micro, LED light treatment, skin needling and retail products.

```html
<!DOCTYPE html>
<html lang="en">
<head>
<meta charset="utf-8">
<title>Velmora Beauty – Business Card</title>
<link rel="stylesheet" href="https://fonts.googleapis.com/css2?family=Great+Vibes&family=Open+Sans:wght@300;400;600&display=swap">
<style>
  :root {
    --backdrop: #e7e3dd;
    --black: #0b0b0b;
    --black-soft: #1c1c1c;
    --gold: #c9952f;
    --gold-light: #f1d27a;
    --gold-mid: #d9ac45;
    --gold-deep: #a8761c;
    --paper: #ffffff;
    --ink: #4a4a4a;
    --bullet: #111111;
  }
  * { box-sizing: border-box; margin: 0; padding: 0; }
  html, body {
    width: 1200px;
    height: 676px;
    overflow: hidden;
    background: var(--backdrop);
  }
  .canvas {
    width: 1200px;
    height: 676px;
    display: flex;
    align-items: center;
    justify-content: center;
    gap: 56px;
  }
  .card {
    position: relative;
    width: 520px;
    height: 318px;
    border-radius: 3px;
    box-shadow: 0 10px 28px rgba(0,0,0,0.18), 0 2px 6px rgba(0,0,0,0.12);
    overflow: hidden;
  }

  /* Front */
  .card-front .glitter-frame {
    position: absolute;
    inset: 0;
    background:
      radial-gradient(circle at 20% 30%, var(--gold-light) 0%, transparent 45%),
      radial-gradient(circle at 80% 75%, var(--gold-light) 0%, transparent 40%),
      linear-gradient(135deg, var(--gold-mid), var(--gold-light) 45%, var(--gold-deep) 100%);
  }
  .card-front .logo-panel {
    position: absolute;
    top: 36px;
    left: 38px;
    right: 38px;
    bottom: 36px;
    background: linear-gradient(160deg, var(--black-soft), var(--black) 60%);
    display: flex;
    align-items: center;
    justify-content: center;
  }
  .brand-name {
    font-family: "Great Vibes", cursive;
    font-weight: 400;
    font-size: 62px;
    color: var(--gold);
    letter-spacing: 0.5px;
  }

  /* Back */
  .card-back {
    background: var(--paper);
    padding: 34px 36px 26px 40px;
    font-family: "Open Sans", sans-serif;
    color: var(--ink);
  }
  .therapist-name {
    font-family: "Great Vibes", cursive;
    font-size: 40px;
    color: var(--gold);
    line-height: 1;
  }
  .therapist-role {
    margin-top: 4px;
    font-size: 13px;
    font-weight: 400;
    letter-spacing: 1px;
    color: var(--gold);
  }
  .services {
    list-style: none;
    margin-top: 18px;
    display: grid;
    grid-template-columns: repeat(3, auto);
    column-gap: 22px;
    row-gap: 5px;
    font-size: 10.5px;
    color: var(--bullet);
  }
  .services li {
    display: flex;
    align-items: center;
    gap: 6px;
    white-space: nowrap;
  }
  .services li::before {
    content: "";
    width: 6px;
    height: 6px;
    background: var(--bullet);
    flex: none;
  }
  .phone {
    margin-top: 24px;
    font-size: 36px;
    font-weight: 300;
    color: var(--ink);
    letter-spacing: 1px;
  }
  .hours {
    margin-top: 12px;
    font-size: 10.5px;
    color: var(--gold);
    line-height: 1.55;
  }
</style>
</head>
<body>
  <main class="canvas">
    <section class="card card-front" aria-label="Card front">
      <div class="glitter-frame" role="img" aria-label="Gold glitter border"></div>
      <div class="logo-panel">
        <span class="brand-name">Velmora Beauty</span>
      </div>
    </section>

    <section class="card card-back" aria-label="Card back">
      <h1 class="therapist-name">Corinne Ashdale</h1>
      <p class="therapist-role">Advanced Beauty Therapist</p>
      <ul class="services">
        <li>Waxing</li>
        <li>Tinting</li>
        <li>Facials</li>
        <li>Swedish Massage</li>
        <li>Hot Stone Massage</li>
        <li>Peels</li>
        <li>LED Light Treatment</li>
        <li>Skin Needling</li>
        <li>Micro</li>
        <li>Retail Products</li>
      </ul>
      <p class="phone">0457 318 042</p>
      <p class="hours">Monday - Friday 9am - 2.30pm<br>Weekends and nights by appointment only</p>
    </section>
  </main>
</body>
</html>
```